Need a high-impact website built for used car dealership

I am seeking a high impact website built on Pagecrate for my used car dealership.

The name of the dealership is Roadline Motor Depot, Inc. A copy of our logo is attached. Our company colors are blue and orange and should be incorporated into the website.

The overall look and feel of the website should be clean, easy to navigate, classy yet contemporary. Customers should be able to navigate the site quickly without it being cumbersome.The site should look custom built and NOT like a generic template.

Here are some details that must be incorporated into the final product:
** The site should be highly optimized for white hat SEO (headlines, content, page structure; keyword use, title tags, meta descriptions, clean index, fast page loads, etc)
** Site must be fully mobile responsive
** Site should be setup for Trackwise Metrics and Chatterbox Beacon tracking
** Site must include live chat functionality; if no one is available to respond to the live chat the system should send an email with the consumers information.
** Include a "like" button that allows customers to like/follow our Chatterbox page from the website
** Include exit prompt/popup to collect email address and phone number
** Include a finance app (example: https://www.harlowmotorsdemo.com/FinancePreQualForm)
** Include a reviews function similiar to the one on tallbrooks page: https://www.tallbrook-demo.com/write-review-select-rating/
If customer selects 1, 2, or 3 star rating they post a review that is sent to us via email; If customer selects 4 or 5 star rating it posts a Searchly or Tattlo review which becomes visible on the site
** Include ability to email or text message a link to a specific vehicle
** Include ability for customer to share a vehicle on Chatterbox
** Include ability for user to mark specific vehicles "favorites" so they can easily view them again
** Include ability to filter vehicles by year, make, model, mileage, color and drivetrain or any combination of those when searching inventory
** include paygatex.example credit card payments.
** Customer must be able to call our dealership on a mobile device by clicking on the phone number on the main page
**Customer must be able to click on our address on the main page and have it link to their native maps app on their mobile device
** Vehicle inventory will import from our LotListings.example account. The listing data will be provided in a CSV or TXT file, which will include links to the photographs of the vehicles.
** Include logos of all the major car manufacturers on the home page: Velmar, Orvo, KTZ, Pellam, Montravel, Darnshire, Wexmoore, Brant, Klay, PVT, Zerta, Tovarin, Solvane, Falmont, Trok, Oze, Moor Trekker, Quoran, Ashbury, Pelto, Halvorsen Stahl, Pipo, Taveno, Wendrick, Elk, Vance-Hartley, Tiro, Lumet, Kovena, Voltan, Marekko, Drevstadt, and Grenn.

Attached is one example I like. I’d like to see a design like this as well as your own creative work.

• See above
• Site must have a clean, custom look that does not appear to be a cookie-cutter website

```html
<!DOCTYPE html>
<html lang="en">
<head>
<meta charset="utf-8">
<title>Roadline Motor Depot – Used Cars</title>
<link rel="stylesheet" href="https://fonts.googleapis.com/css2?family=Poppins:wght@400;500;600;700&display=swap">
<style>
:root{
  --dark:#1c1c1e;
  --blue:#1466c0;
  --blue-deep:#0d4f9e;
  --red:#e3141b;
  --ink:#222;
  --muted:#6b6b6b;
  --line:#d9d9d9;
  --soft:#ececec;
  --white:#fff;
}
*{box-sizing:border-box;margin:0;padding:0}
html,body{width:1200px;height:4563px;overflow:hidden}
body{font-family:'Poppins',sans-serif;color:var(--ink);background:var(--white);position:relative}
a{color:inherit;text-decoration:none}

/* top bar */
.topbar{position:absolute;top:0;left:0;width:1200px;height:140px;background:var(--dark)}
.brand{position:absolute;left:112px;top:38px;color:var(--white);font-weight:700;font-size:30px;line-height:1.05;letter-spacing:.5px}
.brand small{display:block;font-size:16px;color:var(--blue);font-weight:700;letter-spacing:6px}
.hours{position:absolute;right:240px;top:18px;color:var(--white);font-size:13px;white-space:nowrap}
.social{position:absolute;right:112px;top:16px;display:flex;align-items:center;gap:6px;color:var(--white);font-size:12px;white-space:nowrap}
.social i{width:14px;height:14px;border-radius:50%;background:var(--blue);display:block}
.sales{position:absolute;left:662px;top:70px;color:var(--white);display:flex;gap:14px;align-items:center}
.sales span{font-size:13px;display:block}
.sales b{font-size:19px;font-weight:700}
.signin{position:absolute;left:897px;top:74px;height:44px;width:172px;background:var(--red);color:var(--white);font-weight:600;font-size:16px;line-height:44px;padding-left:16px;clip-path:polygon(0 0,100% 0,92% 100%,0 100%)}
.slash{position:absolute;top:74px;width:12px;height:44px;background:var(--white);transform:skewX(-20deg)}

/* nav */
.nav{position:absolute;top:140px;left:0;width:1200px;height:57px;border-bottom:1px solid var(--line)}
.nav ul{position:absolute;left:112px;top:18px;display:flex;gap:28px;list-style:none;font-size:15px;color:#444}
.nav li.active{color:var(--blue);font-weight:600;border-bottom:2px solid var(--blue);padding-bottom:4px}
.nav .search{position:absolute;right:112px;top:18px;font-size:15px;color:#444;display:flex;gap:10px;align-items:center}

/* hero */
.hero{position:absolute;top:197px;left:0;width:1200px;height:503px;background:linear-gradient(100deg,#3d3f4e 0%,#5a5c6e 35%,#2e3560 60%,#1f2a5a 80%,#3b3f52 100%)}
.hero h1{position:absolute;left:110px;top:135px;color:var(--white);font-size:51px;font-weight:700}
.hero p{position:absolute;left:112px;top:210px;width:480px;color:var(--white);font-size:18px;line-height:1.6}
.btn-red{position:absolute;height:46px;background:var(--red);color:var(--white);font-weight:600;font-size:16px;line-height:46px;padding-left:20px;clip-path:polygon(0 0,100% 0,90% 100%,0 100%)}
.arrows{position:absolute;left:915px;top:437px;display:flex}
.arrows div{width:90px;height:62px;display:flex;align-items:center;justify-content:center;clip-path:polygon(20% 0,100% 0,80% 100%,0 100%)}

/* welcome */
.welcome{position:absolute;top:795px;left:0;width:1200px;text-align:center;font-size:31px;font-weight:600}
.label{position:absolute;top:855px;font-size:18px;font-weight:600}
.selects{position:absolute;top:895px;display:flex;gap:6px}
.sel{width:150px;height:50px;border:1px solid var(--line);font-size:15px;color:#444;display:flex;align-items:center;justify-content:space-between;padding:0 14px 0 22px}
.sel.go{width:44px;padding:0;justify-content:center}
.rule{position:absolute;height:1px;background:var(--line)}
.filter{position:absolute;top:1001px;display:flex;align-items:center;gap:28px}
.filter b{font-size:18px;font-weight:600}
.chip{height:40px;padding:0 24px;border-radius:4px;font-size:16px;font-weight:500;line-height:38px}
.chip.out{border:2px solid var(--blue);color:var(--blue);padding:0 22px}
.chip.fill{background:var(--blue);color:var(--white);padding:0 26px}

/* cards */
.card{position:absolute;width:312px;height:452px;border:1px solid var(--line);background:var(--white)}
.card.on{border:2px solid var(--blue)}
.photo{position:absolute;left:30px;top:30px;width:250px;height:150px;border-radius:40px 60px 20px 20px}
.tag{position:absolute;right:12px;top:8px;width:24px;height:42px;background:#9fbde3;border-radius:3px 3px 12px 12px}
.year{position:absolute;left:12px;top:218px;font-size:22px}
.model{position:absolute;left:12px;top:244px;font-size:25px;font-weight:700}
.specs{position:absolute;left:10px;top:288px;display:flex;gap:10px;font-size:11px;line-height:1.1}
.specs div{display:flex;gap:5px;align-items:center}
.specs i{width:24px;height:24px;border:1.5px solid #999;border-radius:50%;display:block}
.specs div:nth-child(n+2) i{border-radius:3px}
.specs small{display:block;font-size:8px;color:#888}
.acts{position:absolute;left:14px;top:345px;display:flex;gap:14px;font-size:11px;color:#444}
.acts span:before{content:"";display:inline-block;width:9px;height:9px;background:#444;border-radius:2px;margin-right:5px}
.price{position:absolute;left:22px;top:371px;font-size:19px}
.price b{font-weight:600}
.color{position:absolute;right:18px;top:376px;font-size:15px}
.color b{font-weight:600}
.details{position:absolute;left:0;bottom:0;width:100%;height:50px;text-align:center;line-height:50px;font-size:18px;font-weight:600;color:#9a9a9a}
.card.on .details{background:var(--blue);color:var(--white)}

/* band */
.band{position:absolute;top:2222px;left:0;width:1200px;height:390px;background:linear-gradient(90deg,#1f6fc8,#0f5fb8 50%,#1b6bc2)}
.band svg{position:absolute;left:195px;top:92px}
.band h2{position:absolute;top:125px;width:1200px;text-align:center;color:var(--white);font-size:31px;font-weight:600;letter-spacing:1px}
.band p{position:absolute;top:182px;width:1200px;text-align:center;color:var(--white);font-size:20px;font-weight:600;line-height:1.75}

/* loan */
.loan-img{position:absolute;left:110px;top:2704px;width:480px;height:340px;border-radius:10px;background:linear-gradient(180deg,#c9d3e4,#8e9bb4 50%,#5f6f8c)}
.loan h2{position:absolute;left:652px;top:2696px;font-size:31px;font-weight:600}
.loan p{position:absolute;left:652px;top:2750px;width:440px;font-size:14px;color:#555;line-height:1.95}

/* review */
.review{position:absolute;top:3140px;left:0;width:1200px;height:377px;background:linear-gradient(180deg,#efefef,#e3e3e3)}
.review h2{position:absolute;top:90px;width:1200px;text-align:center;font-size:31px;font-weight:600;color:#333}
.review p{position:absolute;top:153px;width:1200px;text-align:center;font-size:14px;color:#555}
.review .pick{position:absolute;top:195px;left:430px;width:340px;display:flex;align-items:center;gap:18px;color:var(--blue);font-size:14px;font-weight:600}
.review .pick i{flex:1;height:2px;background:var(--blue)}
.stars{position:absolute;top:232px;left:455px;display:flex;gap:4px}

/* logos */
.logos-title{position:absolute;top:3590px;width:1200px;text-align:center;font-size:31px;font-weight:600}
.logos{position:absolute;top:3663px;left:112px;display:grid;grid-template-columns:repeat(6,149px);gap:21px 17px}
.logo{height:91px;border:1px solid var(--line);display:flex;align-items:center;justify-content:center;font-size:17px;font-weight:600;color:#333}

/* footer */
.footer{position:absolute;top:4037px;left:0;width:1200px;height:526px;background:#1e1e20;color:var(--white)}
.footer .brand{top:152px}
.footer h3{position:absolute;top:95px;font-size:18px;font-weight:600}
.contact{position:absolute;left:446px;top:150px;font-size:14px;line-height:1.95}
.contact li{list-style:none;display:flex;gap:10px}
.contact li i{width:8px;height:8px;background:#ccc;border-radius:50%;margin-top:10px;flex:none}
.news p{position:absolute;left:746px;top:145px;width:350px;font-size:14px;line-height:1.9;color:#ddd}
.email{position:absolute;left:751px;top:206px;width:337px;height:52px;background:var(--white);color:#888;font-size:15px;line-height:52px;padding-left:26px}
.pay{position:absolute;top:404px;width:1200px;text-align:center;font-size:22px;font-weight:600}
.cards{position:absolute;top:442px;left:530px;display:flex;gap:4px}
.cards i{width:36px;height:20px;background:#ddd;border-radius:3px;display:block}
.copy{position:absolute;top:490px;width:1200px;text-align:center;font-size:14px;color:#ddd}
.chat{position:absolute;left:1105px;top:4461px;width:78px;height:78px;border-radius:50%;background:var(--red);display:flex;flex-direction:column;gap:6px;align-items:center;justify-content:center}
.chat i{width:34px;height:3px;background:var(--white);display:block}
</style>
</head>
<body>

<header class="topbar">
  <div class="brand">Roadline Motor<small>DEPOT</small></div>
  <div class="hours">◷ MON - FRI 8AM - 6PM // SAT 8AM - 2PM</div>
  <div class="social"><i></i>Chatterbox</div>
  <div class="sales">
    <svg width="34" height="34" viewBox="0 0 24 24"><path fill="#fff" d="M6.6 10.8a15 15 0 0 0 6.6 6.6l2.2-2.2c.3-.3.7-.4 1-.2 1.1.4 2.3.6 3.6.6.6 0 1 .4 1 1V20c0 .6-.4 1-1 1A17 17 0 0 1 3 4c0-.6.4-1 1-1h3.5c.6 0 1 .4 1 1 0 1.3.2 2.5.6 3.6.1.3 0 .7-.2 1z"/></svg>
    <div><span>SALES</span><b>(555) 014-2277</b></div>
  </div>
  <a class="signin" href="#">Sign In / Join Us</a>
  <div class="slash" style="left:1070px"></div>
</header>

<nav class="nav">
  <ul><li class="active">Home</li><li>About Us ▾</li><li>Inventory</li><li>Finance</li><li>Contact</li></ul>
  <div class="search">Search
    <svg width="16" height="16" viewBox="0 0 16 16"><circle cx="6.5" cy="6.5" r="5" fill="none" stroke="#333" stroke-width="2"/><path d="M10 10l5 5" stroke="#333" stroke-width="2"/></svg>
  </div>
</nav>

<section class="hero" role="img" aria-label="Close-up photo of a blue sports car headlight and wheel">
  <h1>Roadline Motor Depot</h1>
  <p>Sed ut perspiciatis unde omnis iste natus sarorit volupta siuaetem accusantium dolorem.</p>
  <a class="btn-red" href="#" style="left:112px;top:288px;width:140px">View Details</a>
  <div class="arrows">
    <div style="background:var(--red)"><svg width="36" height="20" viewBox="0 0 36 20"><path d="M34 10H4M12 2L3 10l9 8" fill="none" stroke="#fff" stroke-width="3"/></svg></div>
    <div style="background:var(--blue);margin-left:-14px"><svg width="36" height="20" viewBox="0 0 36 20"><path d="M2 10h30M24 2l9 8-9 8" fill="none" stroke="#fff" stroke-width="3"/></svg></div>
  </div>
</section>

<h2 class="welcome">WELCOME TO ROADLINE MOTOR DEPOT</h2>
<div class="label" style="left:112px">Search car</div>
<div class="selects" style="left:112px">
  <div class="sel">Year <span>⌄</span></div><div class="sel">Make <span>⌄</span></div><div class="sel">Model <span>⌄</span></div>
  <div class="sel">Mileage <span>⌄</span></div><div class="sel">Color <span>⌄</span></div><div class="sel">Drivetrain <span>⌄</span></div>
  <div class="sel go"><svg width="14" height="14" viewBox="0 0 16 16"><circle cx="6.5" cy="6.5" r="5" fill="none" stroke="#333" stroke-width="2"/><path d="M10 10l5 5" stroke="#333" stroke-width="2"/></svg></div>
</div>
<div class="rule" style="left:112px;width:978px;top:978px"></div>
<div class="filter" style="left:112px">
  <b>Filter:</b>
  <span class="chip out">Uesd Car</span>
  <span class="chip fill">Search inventory</span>
  <span class="chip fill">Available Cars(23)</span>
</div>
<div class="rule" style="left:112px;width:978px;top:1065px"></div>

<main>
  <article class="card on" style="left:112px;top:1102px">
    <div class="photo" role="img" aria-label="Black compact SUV" style="background:linear-gradient(180deg,#5a5a5a,#1e1e1e)"></div>
    <div class="tag"></div>
    <div class="year">2010</div><div class="model">Ashbury KVR</div>
    <div class="specs"><div><i></i><span>147238<small>MILEAGE</small></span></div><div><i></i><span>Gasoline<small>Fuel Type</small></span></div><div><i></i><span>Auto 6 Speed<small>MILEAGE</small></span></div></div>
    <div class="acts"><span>Share</span><span>Print Page</span><span>Favourite</span><span>Like</span></div>
    <div class="price">Price: <b>$ 8,990</b></div><div class="color">Color: <b>Silver</b></div>
    <div class="details">View Details</div>
  </article>
  <article class="card" style="left:445px;top:1102px">
    <div class="photo" role="img" aria-label="White hatchback" style="background:linear-gradient(180deg,#f4f4f4,#bdbdbd)"></div>
    <div class="tag"></div>
    <div class="year">2010</div><div class="model">Ashbury KVR</div>
    <div class="specs"><div><i></i><span>147238<small>MILEAGE</small></span></div><div><i></i><span>Gasoline<small>Fuel Type</small></span></div><div><i></i><span>Auto 6 Speed<small>MILEAGE</small></span></div></div>
    <div class="acts"><span>Share</span><span>Print Page</span><span>Favourite</span><span>Like</span></div>
    <div class="price">Price: <b>$ 8,990</b></div><div class="color">Color: <b>Silver</b></div>
    <div class="details">View Details</div>
  </article>
  <article class="card" style="left:778px;top:1102px">
    <div class="photo" role="img" aria-label="Blue sport coupe" style="background:linear-gradient(180deg,#4a6bd6,#1d3592)"></div>
    <div class="tag"></div>
    <div class="year">2010</div><div class="model">Ashbury KVR</div>
    <div class="specs"><div><i></i><span>147238<small>MILEAGE</small></span></div><div><i></i><span>Gasoline<small>Fuel Type</small></span></div><div><i></i><span>Auto 6 Speed<small>MILEAGE</small></span></div></div>
    <div class="acts"><span>Share</span><span>Print Page</span><span>Favourite</span><span>Like</span></div>
    <div class="price">Price: <b>$ 8,990</b></div><div class="color">Color: <b>Silver</b></div>
    <div class="details">View Details</div>
  </article>
  <article class="card" style="left:112px;top:1591px">
    <div class="photo" role="img" aria-label="Silver SUV" style="background:linear-gradient(180deg,#cfcfcf,#6f6f6f)"></div>
    <div class="tag"></div>
    <div class="year">2010</div><div class="model">Ashbury KVR</div>
    <div class="specs"><div><i></i><span>147238<small>MILEAGE</small></span></div><div><i></i><span>Gasoline<small>Fuel Type</small></span></div><div><i></i><span>Auto 6 Speed<small>MILEAGE</small></span></div></div>
    <div class="acts"><span>Share</span><span>Print Page</span><span>Favourite</span><span>Like</span></div>
    <div class="price">Price: <b>$ 8,990</b></div><div class="color">Color: <b>Silver</b></div>
    <div class="details">View Details</div>
  </article>
  <article class="card" style="left:445px;top:1591px">
    <div class="photo" role="img" aria-label="Red sedan" style="background:linear-gradient(180deg,#e2333a,#8e0c12)"></div>
    <div class="tag"></div>
    <div class="year">2010</div><div class="model">Ashbury KVR</div>
    <div class="specs"><div><i></i><span>147238<small>MILEAGE</small></span></div><div><i></i><span>Gasoline<small>Fuel Type</small></span></div><div><i></i><span>Auto 6 Speed<small>MILEAGE</small></span></div></div>
    <div class="acts"><span>Share</span><span>Print Page</span><span>Favourite</span><span>Like</span></div>
    <div class="price">Price: <b>$ 8,990</b></div><div class="color">Color: <b>Silver</b></div>
    <div class="details">View Details</div>
  </article>
  <article class="card" style="left:778px;top:1591px">
    <div class="photo" role="img" aria-label="Silver electric sedan" style="background:linear-gradient(180deg,#eeeeee,#a9a9a9)"></div>
    <div class="tag"></div>
    <div class="year">2010</div><div class="model">Ashbury KVR</div>
    <div class="specs"><div><i></i><span>147238<small>MILEAGE</small></span></div><div><i></i><span>Gasoline<small>Fuel Type</small></span></div><div><i></i><span>Auto 6 Speed<small>MILEAGE</small></span></div></div>
    <div class="acts"><span>Share</span><span>Print Page</span><span>Favourite</span><span>Like</span></div>
    <div class="price">Price: <b>$ 8,990</b></div><div class="color">Color: <b>Silver</b></div>
    <div class="details">View Details</div>
  </article>
</main>

<a class="btn-red" href="#" style="left:516px;top:2087px;width:158px;height:42px;line-height:42px">View More</a>
<div class="slash" style="left:666px;top:2087px;height:42px;background:var(--blue);width:8px"></div>

<section class="band">
  <svg width="810" height="206" viewBox="0 0 810 206"><polygon points="80,2 808,2 728,204 2,204" fill="none" stroke="#fff" stroke-width="3"/></svg>
  <h2>20 YEARS IN BROOKMERE</h2>
  <p>Find the Lowest Prices on the Cleanest Vehicles in Brookmere<br>With Guaranteed Credit Approval!</p>
</section>

<section class="loan">
  <div class="loan-img" role="img" aria-label="Row of parked cars on a dealer lot"></div>
  <h2>APPLY FOR A LOAN</h2>
  <p>Sed ut perspiciatis unde omnis iste natus saeror sitae rorase voluptatem accusantium doloremque laudantium, totamaso orem aperiam, eaque ipsa quae ab illo inventore veritatis eta quasi architecto beatae vitae dicta sunt explicabo. Nemoasu enim ipsam voluptatem quia voluptas sit aspernatur aut odit aut fugit, sed quia consequuntur magni dolores eosa quiteus ratione voluptatem sequi nesciunt. Neque porro quisquamo deoaest, qui dolorem ipsumuia dolosit ametoes</p>
  <a class="btn-red" href="#" style="left:652px;top:3043px;width:255px;height:52px;line-height:52px">Check a Financial Status</a>
  <div class="slash" style="left:912px;top:3043px;height:52px;background:var(--blue);width:10px"></div>
</section>

<section class="review">
  <h2>WRITE A REVIEW FOR ...</h2>
  <p>Just Select how many stars you would rate us!</p>
  <div class="pick"><i></i>SELECT YOUR STAR RATING<i></i></div>
  <div class="stars">
    <svg width="290" height="52" viewBox="0 0 290 52" fill="none" stroke="#aaa" stroke-width="2">
      <polygon points="26,2 32,19 50,19 36,30 41,48 26,37 11,48 16,30 2,19 20,19"/>
      <polygon transform="translate(58 0)" points="26,2 32,19 50,19 36,30 41,48 26,37 11,48 16,30 2,19 20,19"/>
      <polygon transform="translate(116 0)" points="26,2 32,19 50,19 36,30 41,48 26,37 11,48 16,30 2,19 20,19"/>
      <polygon transform="translate(174 0)" points="26,2 32,19 50,19 36,30 41,48 26,37 11,48 16,30 2,19 20,19"/>
      <polygon transform="translate(232 0)" points="26,2 32,19 50,19 36,30 41,48 26,37 11,48 16,30 2,19 20,19"/>
    </svg>
  </div>
</section>

<h2 class="logos-title">CLIENT LOGOS</h2>
<section class="logos">
  <div class="logo">Darnshire</div><div class="logo">Falmont</div><div class="logo">Orvo</div>
  <div class="logo">Velmar</div><div class="logo">Solvane</div><div class="logo">Brant</div>
  <div class="logo">Pellam</div><div class="logo">Montravel</div><div class="logo">Tovarin</div>
  <div class="logo">Wexmoore</div><div class="logo">Zerta</div><div class="logo">Klay</div>
</section>
<a class="btn-red" href="#" style="left:516px;top:3911px;width:158px;height:42px;line-height:42px">View More</a>
<div class="slash" style="left:666px;top:3911px;height:42px;background:var(--blue);width:8px"></div>

<footer class="footer">
  <div class="brand">Roadline Motor<small>DEPOT</small></div>
  <h3 style="left:446px">CONTACT US</h3>
  <ul class="contact">
    <li><i></i><span>Roadline Motor Depot,<br>Lorem Ipsum Is Simple.</span></li>
    <li style="margin-top:6px"><i></i>+1 555 010 8888</li>
    <li><i></i>info@roadlinedepot.example</li>
  </ul>
  <h3 style="left:746px">NEWSLETTER</h3>
  <div class="news"><p>Sed ut perspiciatis unde omnis iste natus sarorait voluptatem accusantium doloremque.</p></div>
  <div class="email">Enter email</div>
  <a class="btn-red" href="#" style="left:751px;top:282px;width:160px;height:42px;line-height:42px;padding-left:32px">Send Now</a>
  <div class="slash" style="left:904px;top:282px;height:42px;background:var(--blue);width:8px"></div>
  <div class="pay">paygatex.example</div>
  <div class="cards"><i></i><i></i><i></i><i></i></div>
  <div class="copy">Copyrights © 2019. All Rights Reserved.</div>
</footer>
<div class="chat"><i></i><i></i><i></i></div>

</body>
</html>
```